K7 Teardown looking for leading edge design not typical for our industry

We need to incorporate our new company tag line "foundations, follow-through, fairness" into our cards. Im open to any type of design for this and colour treatment. In fact the whole card needs a new lay out including the back. "Sustainable Deconstruction" needs to be removed from the back and the new tagline used. Would like to see different text and treatment used for "Deconstruction & Demolition".

Target Market(s)

Construction

Industry/Entity Type

Construction Company

Contact Information for Business Card

Standard business card size

Font styles to use
Sans Serif

Colors
9bcb3c
0255a3
f37122

Requirements
Should not have
• Irregular sizing.

```html
<!DOCTYPE html>
<html lang="en">
<head>
<meta charset="utf-8">
<title>K7 Teardown – Business Cards</title>
<link rel="stylesheet" href="https://fonts.googleapis.com/css2?family=Open+Sans:wght@400;600;700&family=Questrial&display=swap">
<style>
  :root {
    --stage: #3a3a3a;
    --paper: #ffffff;
    --lime: #a4c84a;
    --lime-light: #b3d35c;
    --teal: #006d77;
    --ink: #555a5e;
    --rule: #d8dcdc;
    --badge: #c9cbcc;
  }
  * { box-sizing: border-box; margin: 0; padding: 0; }
  html, body { width: 1200px; height: 659px; overflow: hidden; }
  body {
    background: var(--stage);
    font-family: "Open Sans", Arial, sans-serif;
    position: relative;
  }
  .card {
    position: absolute;
    top: 180px;
    width: 520px;
    height: 298px;
    overflow: hidden;
    box-shadow: 0 6px 18px rgba(0,0,0,.35);
  }

  /* Front */
  .card--front { left: 50px; background: var(--paper); }
  .front__brand {
    position: absolute; left: 34px; top: 56px; width: 210px;
    display: flex; align-items: center; gap: 12px;
  }
  .brand__dot {
    width: 40px; height: 40px; border-radius: 50%;
    background: var(--lime); flex: none;
  }
  .brand__name {
    font-family: "Questrial", Arial, sans-serif;
    font-size: 15px; line-height: 1.2; color: var(--teal);
    text-transform: uppercase; letter-spacing: .5px;
  }
  .front__badge {
    position: absolute; left: 60px; top: 140px;
    width: 84px; height: 56px;
    background: var(--badge);
  }
  .front__divider {
    position: absolute; left: 258px; top: 30px; width: 1px; height: 170px;
    background: var(--rule);
  }
  .contact { position: absolute; left: 282px; top: 34px; color: var(--ink); }
  .contact__name { font-size: 18px; font-weight: 600; color: var(--teal); }
  .contact__title { font-size: 12px; color: var(--lime); margin-bottom: 10px; }
  .contact__address { font-size: 10.5px; line-height: 1.45; margin-bottom: 8px; }
  .contact__list { list-style: none; font-size: 10.5px; line-height: 1.6; }
  .contact__list li { display: flex; align-items: center; gap: 7px; }
  .contact__list svg { width: 10px; height: 10px; fill: var(--teal); flex: none; }

  .front__band {
    position: absolute; right: 0; bottom: 26px;
    width: 262px; height: 34px;
    background: var(--teal);
    clip-path: polygon(0 0, 100% 0, 100% 100%, 0 100%, 14px 50%);
    padding: 0 18px 0 30px;
    text-align: right;
    font-family: "Questrial", Arial, sans-serif;
    font-size: 12px; line-height: 34px; letter-spacing: 2px; color: #fff;
    white-space: nowrap;
  }
  .front__stripe {
    position: absolute; left: 0; bottom: 0; width: 100%; height: 26px;
    background: var(--lime);
  }

  /* Back */
  .card--back { left: 630px; background: var(--lime); }
  .back__circle {
    position: absolute; left: 40px; top: -70px;
    width: 230px; height: 230px; border-radius: 50%;
    background: var(--lime-light);
  }
  .back__name {
    position: absolute; left: 40px; top: 186px;
    font-family: "Questrial", Arial, sans-serif;
    font-size: 22px; color: var(--teal);
    text-transform: uppercase; letter-spacing: 1px;
  }
  .back__tagline {
    position: absolute; left: 40px; top: 226px;
    font-family: "Questrial", Arial, sans-serif;
    font-size: 15px; color: var(--teal);
    text-transform: capitalize;
  }
</style>
</head>
<body>

<section class="card card--front" aria-label="Business card front">
  <div class="front__brand">
    <span class="brand__dot"></span>
    <span class="brand__name">K7 Teardown &amp; Demolition Inc.</span>
  </div>
  <div class="front__badge" role="img" aria-label="Award badge"></div>

  <div class="front__divider"></div>

  <div class="contact">
    <p class="contact__name">Marcus Hale</p>
    <p class="contact__title">Head Estimator</p>
    <p class="contact__address">#200, 4410-87 Street<br>Red Deer, AB T4N 1K3</p>
    <ul class="contact__list">
      <li><svg viewBox="0 0 10 10"><path d="M2 0.5 3.6 2.6 2.7 3.6C3.3 5 4.8 6.6 6.4 7.3L7.4 6.4 9.5 8 8.3 9.5C4.5 9.2 0.8 5.5 0.5 1.7Z"/></svg>(403) 555.0182</li>
      <li><svg viewBox="0 0 10 10"><path d="M2.5 0h5v10h-5zM3.3 1v7h3.4V1z"/></svg>(403) 555.0147</li>
      <li><svg viewBox="0 0 10 10"><path d="M0 3h10v6H0zM2 0h6v3H2zM1.5 5h2v1h-2z"/></svg>(403) 555.0190</li>
      <li><svg viewBox="0 0 10 10"><path d="M0 1.5h10v7H0zM1 2.5 5 5.5 9 2.5z" fill-rule="evenodd"/></svg>mhale@k7teardown.com</li>
    </ul>
  </div>

  <p class="front__band">WWW.K7TEARDOWN.COM</p>
  <div class="front__stripe"></div>
</section>

<section class="card card--back" aria-label="Business card back">
  <div class="back__circle"></div>
  <p class="back__name">K7 Teardown &amp; Demolition Inc.</p>
  <p class="back__tagline">Foundations, follow-through, fairness</p>
</section>

</body>
</html>
```